Business Card

Please design a business card with our logo on a cream coloured background and include the following information:

Tallowmere Shopping Centre
ph (08) 9314 8806

sales@quillmeadowflorist.com

www.quillmeadowflorist.com

on reverse:

Find us on Petalbook
petalbook.com/quillmeadowflorist

```html
<!DOCTYPE html>
<html lang="en">
<head>
<meta charset="utf-8">
<title>Quillmeadow Florist – Business Card</title>
<link rel="stylesheet" href="https://fonts.googleapis.com/css2?family=Ubuntu+Condensed&family=Ubuntu:wght@400&display=swap">
<style>
  :root {
    --backdrop: #222222;
    --card: #e8d3ad;
    --card-edge: #dcc59c;
    --ink: #3d3b3a;
    --leaf: #4f7d2a;
    --rule: #6b6860;
  }
  * { box-sizing: border-box; margin: 0; padding: 0; }
  html, body { width: 1200px; height: 896px; overflow: hidden; }
  body {
    position: relative;
    background: var(--backdrop);
    font-family: "Ubuntu", sans-serif;
    color: var(--ink);
  }
  .card {
    position: absolute;
    left: 353px;
    width: 485px;
    height: 268px;
    background: linear-gradient(135deg, var(--card) 0%, var(--card-edge) 100%);
  }
  .card--front { top: 165px; }
  .card--back { top: 473px; }

  /* Front */
  .front-brand {
    position: absolute;
    left: 0;
    width: 302px;
    top: 62px;
    text-align: center;
  }
  .brand-dot {
    display: block;
    width: 40px;
    height: 40px;
    margin: 0 auto 18px;
    border-radius: 50%;
    background: var(--leaf);
  }
  .brand-name {
    font-family: "Ubuntu Condensed", "Ubuntu", sans-serif;
    font-size: 28px;
    line-height: 1;
    white-space: nowrap;
    color: var(--ink);
  }
  .social {
    position: absolute;
    left: 0;
    width: 302px;
    top: 204px;
    text-align: center;
    font-size: 15px;
    line-height: 19px;
    white-space: nowrap;
  }

  /* Back */
  .back-brand {
    position: absolute;
    left: 34px;
    top: 54px;
    display: flex;
    align-items: center;
    gap: 12px;
  }
  .back-brand .brand-dot { width: 28px; height: 28px; margin: 0; }
  .back-brand .brand-name { font-size: 25px; color: var(--leaf); }
  .location {
    position: absolute;
    left: 220px;
    top: 158px;
    font-size: 15px;
    letter-spacing: 0.3px;
    text-transform: uppercase;
    white-space: nowrap;
  }
  .location-rule {
    position: absolute;
    left: 212px;
    right: 0;
    top: 184px;
    height: 1px;
    background: var(--rule);
  }
  .contact {
    position: absolute;
    left: 220px;
    top: 196px;
    list-style: none;
    font-size: 13px;
    line-height: 19.5px;
    white-space: nowrap;
  }
</style>
</head>
<body>
  <section class="card card--front" aria-label="Card front">
    <div class="front-brand">
      <span class="brand-dot"></span>
      <p class="brand-name">Quillmeadow Florist</p>
    </div>
    <p class="social">Find us on Petalbook<br>petalbook.com/quillmeadowflorist</p>
  </section>

  <section class="card card--back" aria-label="Card back">
    <div class="back-brand">
      <span class="brand-dot"></span>
      <p class="brand-name">Quillmeadow Florist</p>
    </div>
    <p class="location">Tallowmere Shopping Centre</p>
    <div class="location-rule"></div>
    <ul class="contact">
      <li>(08) 9314 8806</li>
      <li>sales@quillmeadowflorist.com</li>
      <li>www.quillmeadowflorist.com</li>
    </ul>
  </section>
</body>
</html>
```